Horse-Related Social Media Web Design

Need a social media web design for the world’s largest horse training program, Brindlow Open Equestrianism. The site features social media components along with educational material and videos with a free downloadable app for horse owners on-the-go. Although members receive a free 30-day membership, they must choose from three levels of membership when they sign up (similar to kinroots.com). The original design was based off of emberlyapp.com.

We would like a mash-up of the sign-up page for Chatterly and Quipster. The home page will feature an intro video, sign-up field and a tag line and sub text such as:
Ready to Connect?
Connect with your horse, yourself, Brindlow members and friends you haven’t yet met.

The final design should communicate a hip, trendy site for horse-minded people.

We need the design only, sliced for the website. We will do all coding ourselves.

The current website is www.brindlowlinkup.com.

Project Deadline Extended
Reason: We've had multiple designers accept the project, but none have submitted designs.

The deadline of our project has been extended, we have guaranteed it and the budget has been raised to $1,250 US.  

We are looking forward to some excellent submissions!
Thank you.

Please think outside the box. The submissions we've received so far look much like our current site. While we would like a clean, simple look, it should also be trendy and convey that the site is fun without implicitly saying so. We will be tailoring down the text and information on the front page and placing the majority of information inside the information pages in the navigation.

Thank you!

Thank you to everyone who has participated in submitting designs for our contest. 

Target Market(s)

Target market is horse owners and lovers across the world. The company has a very international market with campuses in the UK and Australia and followers literally across the world.

Industry/Entity Type

Training

Requirements
Nice to have
• Please explain why you made certain design choices from a useability perspective when you submit the design.

```html
<!DOCTYPE html>
<html lang="en">
<head>
<meta charset="utf-8">
<title>Brindlow Member – Ready to Connect?</title>
<link rel="stylesheet" href="https://fonts.googleapis.com/css2?family=Source+Sans+3:wght@400;600;700&display=swap">
<style>
:root{
  --navy:#2d3a79;
  --navy-deep:#243068;
  --gold:#f4c244;
  --white:#ffffff;
  --panel:#ebebeb;
  --form-bg:#d8d8d8;
  --ink:#2a2a2a;
  --link:#2f3f8a;
  --btn-top:#4a6fbf;
  --btn-bottom:#233a8a;
}
*{box-sizing:border-box;margin:0;padding:0}
html,body{width:1200px;height:983px;overflow:hidden;background:var(--white)}
body{position:relative;font-family:"Source Sans 3",Arial,sans-serif;color:var(--ink)}

.site-header{position:absolute;left:0;top:0;width:1200px;height:120px;background:var(--navy)}
.member-badge{position:absolute;left:35px;top:9px;width:144px;height:143px;border:4px solid var(--white);border-radius:10px;background:var(--navy);z-index:3;box-shadow:0 2px 4px rgba(0,0,0,.25);text-align:center;overflow:hidden}
.member-badge__ribbon{background:var(--navy-deep);padding:6px 0 5px;color:var(--gold);font-weight:700;line-height:1}
.member-badge__ribbon .big{display:block;font-size:19px}
.member-badge__ribbon .small{display:block;font-size:10px;color:var(--white);margin-top:2px}
.member-badge__mark{display:block;width:26px;height:26px;margin:12px auto 6px;border-radius:50%;background:var(--gold)}
.member-badge__name{font-size:26px;font-weight:400;color:var(--white);line-height:1}

.language-select{position:absolute;left:987px;top:20px;width:178px;height:24px;background:var(--white);border:1px solid #c7c7c7;font-size:12px;color:#888;padding:4px 6px}
.language-select svg{position:absolute;right:6px;top:8px}

.main-nav{position:absolute;top:82px;left:0;width:1200px;height:38px}
.main-nav a{position:absolute;top:0;height:38px;line-height:40px;font-size:17px;color:var(--white);text-decoration:none;transform:translateX(-50%);white-space:nowrap}
.main-nav a.is-active{background:var(--white);color:var(--navy);width:95px;text-align:center;left:554px}

.hero{position:absolute;left:32px;top:131px;width:1133px;height:396px;background:linear-gradient(180deg,#2f4a25 0%,#4d6b35 30%,#8a9c66 45%,#b7a98a 62%,#c3b096 100%)}
.hero__title{position:absolute;left:53px;top:163px;font-size:46px;font-weight:400;color:var(--white);letter-spacing:.5px;line-height:1}
.hero__sub{position:absolute;left:32px;top:212px;width:474px;height:52px;background:rgba(30,30,30,.55);color:var(--white);font-size:18.5px;line-height:22px;padding:3px 0 0 21px}

.content-band{position:absolute;left:0;top:541px;width:1200px;height:371px;background:var(--panel)}

.intro-video{position:absolute;left:43px;top:558px;width:623px;height:334px;background:#000}
.intro-video__play{position:absolute;left:298px;top:138px}
.video-controls{position:absolute;left:0;bottom:0;width:623px;height:32px;background:linear-gradient(#f2f2f2,#d4d4d4);border:1px solid #b5b5b5;display:flex;align-items:center;font-size:15px;font-weight:700;color:#222}
.video-controls .ctl{height:100%;display:flex;align-items:center;justify-content:center;border-right:1px solid #b5b5b5}
.video-controls .time{padding:0 12px}
.video-controls .track{flex:1;height:6px;background:#a8a8a8;border-radius:3px}

.login{position:absolute;left:720px;top:553px;width:431px}
.login__title{font-size:25px;font-weight:400;color:var(--navy);line-height:1}
.login__hint{position:absolute;right:4px;top:16px;font-size:14px;color:var(--link)}
.login__form{position:absolute;left:0;top:37px;width:431px;height:144px;background:var(--form-bg)}
.login__label{position:absolute;left:24px;font-size:17px;color:var(--ink)}
.login__input{position:absolute;left:149px;width:255px;height:29px;background:var(--white);border:1px solid #bdbdbd}
.login__forgot{position:absolute;left:150px;top:108px;font-size:14px;color:var(--link)}
.login__submit{position:absolute;left:314px;top:105px;width:84px;height:24px;border-radius:12px;background:linear-gradient(var(--btn-top),var(--btn-bottom));color:var(--white);font-size:14px;text-align:center;line-height:24px}

.signup-cta{position:absolute;left:780px;top:772px;width:319px;height:70px;border-radius:12px;background:linear-gradient(var(--btn-top),var(--btn-bottom));color:var(--white);font-size:35px;font-weight:700;text-align:center;line-height:68px;box-shadow:0 2px 3px rgba(0,0,0,.2)}
.signup-note{position:absolute;left:780px;top:850px;width:319px;text-align:center;font-size:24px;color:var(--navy)}
.signup-note b{font-weight:700}

.site-footer{position:absolute;left:0;top:912px;width:1200px;height:71px;background:var(--navy);color:var(--white);font-size:11.5px}
.site-footer .copyright{position:absolute;left:32px;top:21px}
.site-footer .legal{position:absolute;left:32px;top:43px}
.site-footer .legal span{margin-right:9px}
</style>
</head>
<body>
<header class="site-header">
  <div class="member-badge">
    <div class="member-badge__ribbon"><span class="big">FREE 30 DAY</span><span class="small">TRIAL MEMBERSHIP!</span></div>
    <span class="member-badge__mark"></span>
    <div class="member-badge__name">Brindlow</div>
  </div>
  <div class="language-select">Select Language
    <svg width="10" height="8" viewBox="0 0 10 8"><path d="M0 0h10L5 8z" fill="#2d3a79"/></svg>
  </div>
  <nav class="main-nav">
    <a class="is-active" href="#">Home</a>
    <a href="#" style="left:662px">Features</a>
    <a href="#" style="left:775px">Pricing</a>
    <a href="#" style="left:873px">Buzz</a>
    <a href="#" style="left:964px">FAQs</a>
    <a href="#" style="left:1081px">Giving Back</a>
  </nav>
</header>

<div class="hero" role="img" aria-label="Photo of a rider standing with a chestnut horse in a show arena, trailers and trees behind"></div>
<h1 class="hero__title">Ready to Connect?</h1>
<p class="hero__sub">Connect with your horse, yourself, Brindlow members and friends you haven’t yet met.</p>

<section class="content-band">
</section>

<div class="intro-video">
  <svg class="intro-video__play" width="26" height="26" viewBox="0 0 26 26"><path d="M2 1l23 12L2 25z" fill="#fff"/></svg>
  <div class="video-controls">
    <div class="ctl" style="width:30px"><svg width="10" height="12" viewBox="0 0 10 12"><path d="M0 0l10 6-10 6z" fill="#222"/></svg></div>
    <span class="time">00:00</span>
    <div class="track"></div>
    <span class="time" style="border-right:1px solid #b5b5b5;height:100%;display:flex;align-items:center">00:00</span>
    <div class="ctl" style="width:72px">
      <svg width="46" height="12" viewBox="0 0 46 12"><path d="M0 4h3v4H0zM3 4l4-3v10L3 8z" fill="#222"/><g fill="#222"><rect x="12" y="5" width="2" height="3"/><rect x="16" y="4" width="2" height="5"/><rect x="20" y="3" width="2" height="7"/><rect x="24" y="2" width="2" height="9"/><rect x="28" y="1" width="2" height="10"/><rect x="32" y="0" width="2" height="12"/><rect x="36" y="0" width="2" height="12"/><rect x="40" y="0" width="2" height="12"/></g></svg>
    </div>
    <div class="ctl" style="width:40px;border-right:0">
      <svg width="16" height="16" viewBox="0 0 16 16" fill="none" stroke="#222" stroke-width="1.6"><path d="M1 5V1h4M11 1h4v4M15 11v4h-4M5 15H1v-4M1 1l5 5M15 1l-5 5M15 15l-5-5M1 15l5-5"/></svg>
    </div>
  </div>
</div>

<section class="login">
  <h2 class="login__title">Member Login</h2>
  <a class="login__hint">Already a member? Sign in</a>
  <div class="login__form">
    <span class="login__label" style="top:27px">Email address</span>
    <span class="login__input" style="top:24px"></span>
    <span class="login__label" style="top:74px">Password</span>
    <span class="login__input" style="top:69px"></span>
    <a class="login__forgot">Forgot Password?</a>
    <span class="login__submit">Submit</span>
  </div>
</section>

<a class="signup-cta">Sign up Now</a>
<p class="signup-note"><b>30</b> Days <b>Free</b> Trial</p>

<footer class="site-footer">
  <p class="copyright">© Copyright 2012 Brindlow Open Equestrianism, Inc. All Rights Reserved.</p>
  <p class="legal"><span>Terms and Conditions of Service</span><span>Privacy Policy</span></p>
</footer>
</body>
</html>
```